依頼概要
■依頼の目的/概要
・電子書籍(自己啓発系)の表紙デザインをお願いします。
・電子書籍は、ソルベリアで販売します。pagoraです。

■本の内容
・初出版本です。
・行き詰った人生を何とかしたいなら、人間関係の苦しみを解消したいなら…。自分の『あり方』を変えることによって、人生がうまくいく方向に動きだすよ ということをお伝えする内容になっています。
・作者の経験が、本の元になっています。
・働く世代や、実際に苦しんでいる当事者、ひきこもりの子どもを持つ親など、幅広く読んでもらいたいです。

■デザイン要望
・明るい未来を感じられるような表紙デザインにしてください。
(底抜けに明るいのは×だけど、悲壮感が見えるのも×)
・人物や、絵が入っている表紙が望ましいです。
(イラスト・写真〇。文字のみのデザインは、×)

■本のタイトル
・本のタイトルは、

毎日が「疲れた…」と感じる君へ、ひとつずつ笑顔が戻ってくる、小さな灯火の地図

です。

・サブキャッチに

~胸のざわめきの理由は〝本音の迷子〟だった~

を入れてください。

■ごあいさつ
・その他、ご不明な点がありましたらお気軽にご質問ください。よろしくお願いします。

■ 選んだ理由

Talkvineをつかって、皆さんからいただいた仮案をアンケートさせていただいたところ、
もっとも「いい」「好き」という評価をいただけたのが、今回選ばせていただいたデザインでした。

なぜよかったのか? と聞いてみたところ
「右下のキャラクターが可愛い」
「見ていると、癒される」
「澄ちゃん(私のこと)らしい」
という意見が、出そろいました。

正直に申しますと、私自身も意外だったのですが
多くの人から「このデザインがいちばん私らしい」と言っていただけるので、気になりはじめ、
今では私自身も気に入っております。

■ 提案者全員のお礼・コメント

本当にありがとうございました。

たった一つのデザインを決めるために、たくさんの方から頂いたデザインを落とさなければならないため、胸を痛めました。
落とすには、あまりにも私好みのデザインがあり過ぎました。

中には私の、初出版の、あまり上手とはいえない文章を丁寧に読んでくれる方もいらっしゃり、とても嬉しかったです。
ありがとうございます。
感謝しています。

また何かの折、お世話になることがあれば、よろしくお願いいたします。

```html
<!DOCTYPE html>
<html lang="ja">
<head>
<meta charset="utf-8">
<title>小さな灯火の地図</title>
<link rel="stylesheet" href="https://fonts.googleapis.com/css2?family=Zen+Maru+Gothic:wght@500;700;900&family=Zen+Old+Mincho:wght@700;900&family=Noto+Serif+JP:wght@700;900&display=swap">
<style>
:root{
  --paper:#eef0f1;
  --bubble:#ffffff;
  --bubble-line:#9aa3ab;
  --ink:#2c3a46;
  --title-ink:#1a1a1a;
  --accent-red:#e2445c;
  --blue:#1f6fb5;
  --band:#1c67ab;
  --band-text:#ffffff;
  --dash:#7fa6c9;
  --leaf:#7cc35a;
  --figure-top:#c9cfd6;
  --figure-bottom:#e3d9df;
  --door:#e9e6df;
}
*{margin:0;padding:0;box-sizing:border-box}
html,body{width:749px;height:1200px;overflow:hidden;background:var(--paper)}
.cover{position:relative;width:749px;height:1200px;overflow:hidden;background:var(--paper);font-family:"Zen Maru Gothic",sans-serif;color:var(--ink)}
.bubble{position:absolute;left:0;top:0}
.lead{position:absolute;left:46px;top:40px}
.lead-top{font-size:46px;font-weight:700;letter-spacing:2px}
.lead-main{display:flex;align-items:flex-end;margin-top:6px}
.lead-big{font-size:86px;font-weight:900;color:var(--ink);line-height:1;letter-spacing:-2px}
.lead-tail{font-size:28px;font-weight:700;margin-left:8px;margin-bottom:10px;line-height:1.2}
.figure-sitting{position:absolute;right:18px;top:8px;width:200px;height:290px;border-radius:40px 40px 20px 20px;background:linear-gradient(180deg,var(--figure-top),var(--figure-bottom))}
.divider{position:absolute;top:345px;height:630px;border-left:4px dashed var(--dash)}
.divider-left{left:290px}
.divider-right{left:380px}
.vertical{position:absolute;writing-mode:vertical-rl;white-space:nowrap}
.title-right{left:598px;top:345px;font-family:"Noto Serif JP",serif;font-weight:900;font-size:70px;color:var(--title-ink);letter-spacing:4px;text-emphasis:filled dot;text-emphasis-color:var(--accent-red);text-emphasis-position:over left}
.title-main{left:440px;top:340px;font-family:"Noto Serif JP",serif;font-weight:900;color:var(--title-ink);line-height:1.05}
.title-main .hero{font-size:128px;color:var(--accent-red)}
.title-main .second{font-size:94px}
.title-main .small{font-size:54px}
.title-main .rest{font-size:62px}
.clover{position:absolute;left:400px;top:470px;width:50px;height:50px;border-radius:50%;background:var(--leaf)}
.subtitle{left:178px;top:360px;font-family:"Zen Old Mincho",serif;font-weight:900;font-size:76px;line-height:1;color:var(--blue);letter-spacing:2px}
.author{left:98px;top:740px;font-family:"Zen Old Mincho",serif;font-weight:700;font-size:46px;line-height:1;color:var(--ink);letter-spacing:6px}
.author-roman{position:absolute;left:28px;top:470px;writing-mode:vertical-rl;font-family:"Zen Maru Gothic",sans-serif;font-size:18px;color:var(--ink);letter-spacing:2px}
.door-character{position:absolute;left:575px;top:775px;width:155px;height:200px;border-radius:14px 14px 0 0;background:linear-gradient(180deg,var(--door),#f6f3ee)}
.band{position:absolute;left:0;top:1000px;width:749px;height:200px;background:var(--band);color:var(--band-text);font-family:"Noto Serif JP",serif;font-weight:900;text-align:center;padding-top:26px}
.band-small{font-size:36px;text-align:left;padding-left:150px;line-height:1.3}
.band-big{font-size:66px;line-height:1.5;letter-spacing:1px}
</style>
</head>
<body>
<main class="cover">
  <svg class="bubble" width="749" height="330" viewBox="0 0 749 330" aria-hidden="true">
    <path d="M30 20 H600 Q620 20 620 40 V235 Q620 255 600 255 H300 L270 300 L262 255 H30 Q10 255 10 235 V40 Q10 20 30 20 Z" fill="var(--bubble)" stroke="var(--bubble-line)" stroke-width="3"/>
  </svg>
  <div class="lead">
    <div class="lead-top">毎日が</div>
    <div class="lead-main">
      <span class="lead-big">「疲れた…」</span>
      <span class="lead-tail">と感じる君へ</span>
    </div>
  </div>
  <div class="figure-sitting" role="img" aria-label="膝を抱えて座り込む人物のイラスト"></div>

  <div class="divider divider-right"></div>
  <div class="divider divider-left"></div>

  <div class="vertical title-right">ひとつずつ</div>
  <div class="vertical title-main"><span class="hero">笑</span><span class="second">顔</span><span class="small">が</span><span class="rest">戻ってくる</span></div>
  <div class="clover" role="img" aria-label="四つ葉のクローバーのイラスト"></div>

  <div class="vertical subtitle">小さな灯火の地図</div>
  <div class="vertical author">秋川 澄央</div>
  <div class="author-roman">Sumio Akikawa</div>

  <div class="door-character" role="img" aria-label="扉から顔を出すカプセル型キャラクターのイラスト"></div>

  <div class="band">
    <div class="band-small">胸のざわめきの理由は</div>
    <div class="band-big">〝本音の迷子〟だった</div>
  </div>
</main>
</body>
</html>
```